Redo website for building and interior design company

I have just got a designer to do my brand new website for a building and interior design business in Brisbane Australia but I'm not very happy with it. I would like some other ideas for how to improve it please. My email signature and business card are attached for existing branding materials.

The website is plovarhomes.com.au

The brief is:
Website inspiration from another building designer about what I do:
https://www.terivobuild.com.au/

Website design inspiration:
no white in background like this: https://pixelfolio.example/shots/40000001-Tailored-apparel-site

use of different brand colours like this one:
https://pixelfolio.example/shots/40000002-Dewmira-Lotion-Site-Layout

https://pixelfolio.example/shots/40000003-Casual-Style-Premium-Trinkets-Home-Screen-Idea

Look and feel for website:
Luxury
Colourful, engaging
Bold
No white backgrounds
Use of copper tones
Mobile friendly
Use brand colours and fonts detailed below

Homepage: To have my logo to introduce the business. Open to different ideas but possibly picture frame in an interior setting with revolving pictures of previous projects like this: https://pixelfolio.example/shots/40000004-Upscale-Property-Site

Logo colour gradient of copper. RGb format
R 245, G 176, B 122
R 158, G 74, B 45
R 119, G 53, B 33

Brand Fonts
Logo font : Dexotick Font
Subtitle font : Phenomena Font

Website Content
• Home
• Who (we are)
• What (we do)
• Why (choose us)
• How (we do it)
o Building Design Process
o Construction Process
o Interior Design Process
• Q and A - Frequently Asked Questions
• (Gallery) Previous projects and examples
• Resources/Blog – Weekly social media posts connected to this
• Reviews/ Testimonials

Target Market(s)

home owners who want to renovate their home

Industry/Entity Type

Building and interior design / architecture

Number of Pages Required

5+ page

Colors
F0912C
F2A743
F7CA91
FBE8D2
FDF5EE
EE7325
F08F49
F5BC92
FAE3D3
FDF4ED

Requirements
Must have
• Thank you for your submissions. Please redo them with more metallic copper variation tones. All of the submissions are very peach and brown. I'd like richer tones and colours. My logo is metallic copper. Also include some gilt tones please. Ive attached examples of metallic copper and copper variation tones to the design brief. Many thanks Marnie
Nice to have
• see brief
Should not have
• see brief

```html
<!DOCTYPE html>
<html lang="en">
<head>
<meta charset="utf-8">
<title>Plovar Designs – Redefining Spaces</title>
<link href="https://fonts.googleapis.com/css2?family=Cinzel:wght@400;500;600&family=Montserrat:wght@400;500;600&family=Saira+Extra+Condensed:wght@300&display=swap" rel="stylesheet">
<style>
:root{
  --copper-deep:#5e2716;
  --copper-dark:#773521;
  --copper:#9e4a2d;
  --copper-mid:#c0673f;
  --copper-light:#f5b07a;
  --gilt:#c9a24a;
  --gilt-light:#ecd08a;
  --champagne:#f3e6d6;
  --champagne-deep:#ead3bb;
  --card:#f9f0e5;
  --rose-copper:#dcae8c;
  --ink:#3a1d12;
  --text:#5a3e32;
  --metal-copper:linear-gradient(135deg,#f5b07a 0%,#c0673f 30%,#9e4a2d 60%,#773521 85%,#5e2716 100%);
  --metal-gilt:linear-gradient(135deg,#ecd08a 0%,#c9a24a 45%,#a67c2e 100%);
  --light:#fdf5ee;
}
*{box-sizing:border-box;margin:0;padding:0}
html,body{width:1200px;height:4874px;overflow:hidden}
body{position:relative;background:var(--champagne);font-family:"Montserrat",sans-serif;color:var(--text)}
.abs{position:absolute}
.heading{font-family:"Cinzel",serif;color:var(--copper-dark);font-weight:500;letter-spacing:1px;white-space:nowrap}
.label{font-size:9px;font-weight:600;color:var(--copper);letter-spacing:.5px;text-transform:uppercase}
.body-text{font-size:11.5px;line-height:1.62;color:var(--text)}
.btn{display:inline-block;background:var(--metal-copper);color:var(--light);font-size:10px;font-weight:600;letter-spacing:.5px;text-align:center;line-height:34px;height:34px;border-bottom:2px solid var(--gilt)}
.ghost{font-family:"Saira Extra Condensed",sans-serif;font-weight:300;letter-spacing:10px;white-space:nowrap;line-height:1;overflow:hidden}
.photo{position:absolute}
.brand{display:flex;align-items:center;gap:8px;font-family:"Cinzel",serif;font-weight:600;color:var(--copper);font-size:20px;white-space:nowrap}
.brand .mark{width:14px;height:14px;background:var(--copper)}
.nav{left:372px;top:44px;display:flex;gap:26px;font-size:9.5px;color:var(--ink)}
.hero-panel{left:935px;top:0;width:265px;height:625px;background:var(--metal-copper)}
.card{background:var(--card);box-shadow:0 4px 16px rgba(94,39,22,.12);border-top:2px solid var(--gilt);padding:22px}
.card h3{font-family:"Cinzel",serif;font-weight:500;font-size:13px;color:var(--ink);margin:16px 0 6px}
.card p{font-size:9.5px;line-height:1.6}
.card a{display:block;margin-top:14px;font-size:8.5px;font-weight:600;color:var(--copper);text-decoration:underline}
.icon{width:46px;height:46px}
.step{left:592px;width:470px}
.step .num{position:absolute;left:0;top:0;width:28px;height:28px;border-radius:50%;background:var(--metal-copper);color:var(--light);font-family:"Cinzel",serif;font-size:15px;text-align:center;line-height:28px;box-shadow:0 0 0 2px var(--gilt-light)}
.step h4{margin-left:40px;font-family:"Cinzel",serif;font-weight:500;font-size:13px;color:var(--ink);margin-bottom:8px;padding-top:5px}
.step p{margin-left:40px;font-size:9.5px;line-height:1.62}
.review{background:var(--card);padding:24px 22px;height:171px;border-top:2px solid var(--gilt);overflow:hidden}
.review .who{display:flex;gap:14px;align-items:center}
.review .avatar{width:54px;height:54px;border-radius:50%;background:linear-gradient(135deg,#b07a5a,#5e2716);box-shadow:0 0 0 2px var(--gilt)}
.review .name{font-family:"Cinzel",serif;font-size:12px;color:var(--ink)}
.review .role{font-size:8.5px;color:var(--copper-mid);margin:3px 0 4px}
.stars{color:var(--gilt);font-size:14px;letter-spacing:4px}
.review p{font-size:9.5px;line-height:1.62;margin-top:16px}
.quote{position:absolute;right:22px;top:18px;font-family:"Cinzel",serif;font-size:70px;line-height:1;color:var(--rose-copper)}
.round-btn{width:38px;height:38px;border-radius:50%;display:flex;align-items:center;justify-content:center}
.faq-item{left:113px;width:445px;height:38px;border:1px solid rgba(236,208,138,.6);display:flex;align-items:center;gap:12px;padding-left:14px;color:var(--light);font-size:9.5px}
.faq-item .plus{width:18px;height:18px;border-radius:50%;background:var(--metal-gilt);color:var(--copper-deep);text-align:center;line-height:18px;font-size:13px}
.post{background:var(--card);box-shadow:0 4px 16px rgba(94,39,22,.12);border-bottom:2px solid var(--gilt)}
.post h5{font-family:"Cinzel",serif;font-weight:500;font-size:13px;color:var(--ink)}
.post p{font-size:9.5px;line-height:1.6;margin-top:8px}
.post a{display:block;margin-top:10px;font-size:8.5px;font-weight:600;color:var(--copper);text-decoration:underline}
.footer-col h6{font-size:9px;font-weight:600;color:var(--gilt-light);letter-spacing:.5px;margin-bottom:18px}
.footer-col li{list-style:none;font-size:9px;color:var(--light);margin-bottom:16px}
.social{width:20px;height:20px;border-radius:50%;background:var(--metal-gilt)}
</style>
</head>
<body>

<!-- HEADER & HERO -->
<div class="abs hero-panel"></div>
<div class="abs brand" style="left:113px;top:46px"><span class="mark"></span>Plovar Designs</div>
<nav class="abs nav"><span>About Us</span><span>Why Choose Us</span><span>What We Do</span><span>Process</span><span>Previous Projects</span></nav>
<svg class="abs" style="left:1010px;top:42px" width="22" height="22" viewBox="0 0 22 22" fill="none" stroke="#fdf5ee" stroke-width="1.6"><circle cx="9" cy="9" r="7"/><path d="M14 14l6 6"/></svg>
<svg class="abs" style="left:1064px;top:44px" width="26" height="18" viewBox="0 0 26 18" stroke="#fdf5ee" stroke-width="1.6"><path d="M0 1h26M0 9h26M0 17h26"/></svg>

<div class="abs label" style="left:113px;top:236px">Redefining Spaces</div>
<h1 class="abs heading" style="left:111px;top:255px;font-size:52px">PLOVAR DESIGNS</h1>
<p class="abs body-text" style="left:113px;top:326px;width:440px;font-size:12.5px">We transform your existing spaces into reflections of your personality and lifestyle. Specialising in renovations, we blend building design and interior design to not just redesign your space, but redefine how you experience it.</p>
<span class="abs btn" style="left:113px;top:422px;width:127px">READ MORE</span>

<div class="abs" style="left:720px;top:170px;width:393px;height:370px;border:1px solid var(--gilt-light)"></div>
<div class="photo" role="img" aria-label="Living room with grey sofa, leaf-print cushions and city view" style="left:693px;top:151px;width:397px;height:371px;background:linear-gradient(135deg,#cdb79b,#6f6a62 55%,#a59a83)"></div>
<div class="abs ghost" style="left:0;top:532px;font-size:110px;color:var(--champagne-deep);width:935px">REDEFINING SPACES</div>

<!-- WHAT WE DO -->
<div class="abs label" style="left:113px;top:685px">Services</div>
<h2 class="abs heading" style="left:111px;top:702px;font-size:36px">WHAT WE DO</h2>

<div class="abs card" style="left:113px;top:767px;width:315px;height:221px">
  <svg class="icon" viewBox="0 0 46 46" fill="none" stroke="var(--copper)" stroke-width="1.6"><rect x="2" y="2" width="30" height="30" fill="var(--champagne-deep)" stroke="none"/><circle cx="24" cy="22" r="9"/><circle cx="24" cy="22" r="3"/><path d="M24 8v4M24 32v4M10 22h4M34 22h4M20 36h8M21 40h6"/></svg>
  <h3>CONCEPT DESIGN</h3>
  <p>Are you ready to kickstart the journey of bringing your vision to life? We start by sitting down with you to understand what you are dreaming of and what you need from your space.</p>
  <a>READ MORE</a>
</div>
<div class="abs card" style="left:443px;top:767px;width:314px;height:221px">
  <svg class="icon" viewBox="0 0 46 46" fill="none" stroke="var(--copper)" stroke-width="1.6"><rect x="2" y="2" width="30" height="30" fill="var(--champagne-deep)" stroke="none"/><rect x="6" y="8" width="36" height="32"/><path d="M14 24l10-8 10 8v10H14z"/><path d="M21 34v-6h6v6"/></svg>
  <h3>DETAILED DRAWINGS</h3>
  <p>This phase is about precision and clarity, turning the broad strokes of our initial concepts into detailed building plans that builders and contractors can follow.</p>
  <a>READ MORE</a>
</div>
<div class="abs card" style="left:772px;top:767px;width:315px;height:221px">
  <svg class="icon" viewBox="0 0 46 46" fill="none" stroke="var(--copper)" stroke-width="1.6"><rect x="2" y="2" width="30" height="30" fill="var(--champagne-deep)" stroke="none"/><rect x="6" y="8" width="34" height="34"/><path d="M12 36l22-22M16 14l16 22M28 12l6 6"/></svg>
  <h3>INTERIOR DESIGN</h3>
  <p>Once the foundation is laid, we delve into the interior design. This involves selecting materials, colours, finishes, and furnishings that align with the overall design concept while catering to your lifestyle and preferences.</p>
  <a>READ MORE</a>
</div>

<!-- WHO WE ARE -->
<div class="abs" style="left:0;top:1051px;width:1200px;height:520px;background:linear-gradient(120deg,#e8bf9f,#dcae8c 60%,#d29a74)"></div>
<div class="abs label" style="left:113px;top:1142px;color:var(--copper-dark)">About Plovar Designs</div>
<h2 class="abs heading" style="left:113px;top:1159px;font-size:36px;color:var(--copper-deep)">WHO WE ARE</h2>
<p class="abs body-text" style="left:113px;top:1213px;width:415px;font-size:9.5px;color:var(--ink)">Founded and led by Marnie Calloway, Plovar Designs is driven by a passion for both the art of design and the science of building. Marnie's design journey is complemented by her hands-on experience in carpentry — a dual expertise that allows us to bridge the gap between conceptual design and practical application, creating a perfect synthesis of form and function.</p>
<p class="abs body-text" style="left:113px;top:1303px;width:415px;font-size:9.5px;color:var(--ink)">Our design philosophy is simple: create with purpose, design with passion. Whether we are drafting building plans or on-site overseeing construction, our multidisciplinary approach ensures that your finished space is uniquely yours. We engage closely with our clients, listening and responding to their needs to ensure that the end result is not only visually pleasing but also perfectly suited to their lifestyle.</p>
<span class="abs btn" style="left:113px;top:1420px;width:120px">READ MORE</span>
<div class="abs" style="left:690px;top:1136px;width:240px;height:374px;border:1px solid var(--copper-dark)"></div>
<div class="photo" role="img" aria-label="Apartment lounge with floor-to-ceiling windows and city towers" style="left:600px;top:1107px;width:242px;height:317px;background:linear-gradient(160deg,#b9c2c4,#6d6a63 55%,#8c7d6c)"></div>
<div class="photo" role="img" aria-label="Bright living room with armchairs and patterned rug" style="left:858px;top:1149px;width:230px;height:373px;background:linear-gradient(160deg,#e7dfd3,#b7a996 55%,#8a8d96)"></div>

<!-- HOW WE DO IT -->
<div class="abs" style="left:87px;top:1636px;width:200px;height:163px;background:var(--metal-copper)"></div>
<div class="photo" role="img" aria-label="Floor lamp beside a sofa with striped navy cushion" style="left:113px;top:1660px;width:407px;height:528px;background:linear-gradient(150deg,#efe9df,#cfc4b5 55%,#8d8a86)"></div>
<div class="abs label" style="left:592px;top:1672px">Process</div>
<h2 class="abs heading" style="left:592px;top:1689px;font-size:36px">HOW WE DO IT</h2>
<div class="abs step" style="top:1750px"><span class="num">1</span><h4>BUILDING DESIGN PROCESS</h4><p>Our building design process begins with understanding your vision and the specifics of your existing space. We conduct a thorough site analysis to gauge both the possibilities and constraints. From there, we develop preliminary designs. Feedback loops are integral, allowing for revisions and refinements until the design perfectly aligns with your expectations. The final design is detailed with technical specifications ready for council approval and construction.</p></div>
<div class="abs step" style="top:1902px"><span class="num">2</span><h4>CONSTRUCTION PROCESS</h4><p>Once the design is finalized and approved, we move forward with securing the necessary permits. Our project management skills come to the forefront, coordinating with contractors, overseeing timelines, and ensuring materials and workmanship are of the highest quality. Regular site visits are conducted to monitor progress, address any issues, and ensure that every aspect of the build adheres to the planned design.</p></div>
<div class="abs step" style="top:2038px"><span class="num">3</span><h4>INTERIOR DESIGN PROCESS</h4><p>Our interior design process is all about bringing personality and functionality together. It starts with an in-depth consultation to understand your style preferences and functional needs. We then create mood boards and colour schemes that reflect your aesthetic while considering the practicality of each space. Selections of furniture, fixtures, and finishes are carefully curated to compliment the design. Throughout the process, we ensure that every element from lighting to layout works harmoniously to create a cohesive and inviting environment.</p></div>

<!-- CLIENT REVIEWS -->
<div class="abs" style="left:0;top:2224px;width:1200px;height:394px;background:var(--champagne-deep)"></div>
<div class="abs label" style="left:113px;top:2280px">Testimonials</div>
<h2 class="abs heading" style="left:113px;top:2297px;font-size:36px">CLIENT REVIEWS</h2>
<p class="abs" style="left:113px;top:2353px;font-size:9.5px">Don't just take our word for it; hear why our clients love working with us!</p>
<div class="abs round-btn" style="left:1004px;top:2300px;border:1.5px solid var(--copper)"><svg width="18" height="10" viewBox="0 0 18 10" fill="none" stroke="var(--copper)" stroke-width="1.5"><path d="M18 5H2M6 1L2 5l4 4"/></svg></div>
<div class="abs round-btn" style="left:1049px;top:2300px;background:var(--metal-copper)"><svg width="18" height="10" viewBox="0 0 18 10" fill="none" stroke="#fdf5ee" stroke-width="1.5"><path d="M0 5h16M12 1l4 4-4 4"/></svg></div>

<div class="abs review" style="left:113px;top:2385px;width:406px"><span class="quote">”</span>
  <div class="who"><div class="avatar" role="img" aria-label="Client portrait"></div><div><div class="name">CORINNE V.</div><div class="role">DESIGNATION</div><div class="stars">★★★★★</div></div></div>
  <p>Working with Marnie and the team at Plovar Designs was a dream come true. They listened attentively to our needs and preferences, and the result exceeded our expectations. Highly recommended!</p></div>
<div class="abs review" style="left:538px;top:2385px;width:405px"><span class="quote">”</span>
  <div class="who"><div class="avatar" role="img" aria-label="Client portrait"></div><div><div class="name">DMITRI K.</div><div class="role">DESIGNATION</div><div class="stars">★★★★★</div></div></div>
  <p>Marnie's innovative approach to interior design transformed our space into a functional and beautiful environment. Her attention to detail and dedication to quality are truly commendable.</p></div>
<div class="abs review" style="left:962px;top:2385px;width:260px"><span class="quote">”</span>
  <div class="who"><div class="avatar" role="img" aria-label="Client portrait"></div><div><div class="name">YVETTE M</div><div class="role">DESIGNATION</div><div class="stars">★★★★★</div></div></div>
  <p style="white-space:nowrap">The project management services provided<br>ensured our renovation was completed smoothly.<br>We appreciated their expertise and communication<br>the process.</p></div>

<!-- FAQ -->
<div class="abs" style="left:0;top:2618px;width:691px;height:587px;background:var(--metal-copper)"></div>
<div class="photo" role="img" aria-label="High-rise living room at dusk with city lights and striped rug" style="left:691px;top:2618px;width:509px;height:587px;background:linear-gradient(160deg,#2e3550,#5c5a66 45%,#cbbfae 75%,#e9e3da)"></div>
<div class="abs label" style="left:113px;top:2698px;color:var(--gilt-light)">FAQ</div>
<h2 class="abs heading" style="left:113px;top:2715px;font-size:36px;color:var(--light);line-height:1.15">FREQUENTLY ASKED<br>QUESTIONS</h2>
<div class="abs faq-item" style="top:2820px"><span class="plus">+</span>What types of projects does Plovar Designs specialize in?</div>
<div class="abs faq-item" style="top:2879px"><span class="plus">+</span>How long does a typical renovation project take from start to finish?</div>
<div class="abs faq-item" style="top:2937px"><span class="plus">+</span>Can Plovar Designs work within my budget?</div>
<div class="abs faq-item" style="top:2996px"><span class="plus">+</span>How involved do I need to be in the design and construction processes?</div>
<div class="abs faq-item" style="top:3055px"><span class="plus">+</span>What makes Plovar Designs different from other design firms?</div>
<div class="abs ghost" style="left:0;top:3130px;font-size:84px;color:rgba(236,208,138,.16);width:691px">REDEFINING SPACES</div>

<!-- LATEST NEWS -->
<div class="abs label" style="left:113px;top:3274px">Blog</div>
<h2 class="abs heading" style="left:111px;top:3291px;font-size:36px">LATEST NEWS</h2>
<p class="abs" style="left:672px;top:3296px;width:420px;font-size:9.5px;line-height:1.6">Whether you are seeking inspiration or practical advice, our posts are here to guide your next project. Happy reading!</p>
<div class="abs post" style="left:113px;top:3360px;width:497px;height:322px">
  <div role="img" aria-label="Modern two-storey home with surrounding trees" style="height:220px;background:linear-gradient(170deg,#6f9ed0,#c9d6de 45%,#6b7d58 80%)"></div>
  <div style="padding:20px 28px"><h5>PLOVAR DESIGN</h5><p>Welcome to Plovar Design This is your first post. Edit or delete it , then start writing!</p><a>LEARN MORE</a></div>
</div>
<div class="abs post" style="left:628px;top:3360px;width:460px;height:155px;display:flex">
  <div role="img" aria-label="Apartment living area with view" style="width:180px;flex:none;background:linear-gradient(150deg,#b9ad99,#6e6e69)"></div>
  <div style="padding:34px 28px"><h5>PLOVAR DESIGN</h5><p>Welcome to Plovar Design This is your first post. Edit or delete it , then start writing!</p><a>LEARN MORE</a></div>
</div>
<div class="abs post" style="left:628px;top:3532px;width:460px;height:150px;display:flex">
  <div role="img" aria-label="Bedroom with navy bedding and ceiling fan" style="width:180px;flex:none;background:linear-gradient(150deg,#e2ddd5,#8d97a6 70%,#26324e)"></div>
  <div style="padding:32px 28px"><h5>PLOVAR DESIGN</h5><p>Welcome to Plovar Design This is your first post. Edit or delete it , then start writing!</p><a>LEARN MORE</a></div>
</div>
<div class="abs ghost" style="left:0;top:3712px;font-size:126px;color:var(--champagne-deep);width:1200px">REDEFINING SPACES</div>

<!-- PREVIOUS PROJECTS -->
<div class="abs label" style="left:107px;top:3876px">Previous Projects</div>
<h2 class="abs heading" style="left:107px;top:3893px;font-size:36px">VISIT OUR BEST PROJECT</h2>
<p class="abs" style="left:672px;top:3896px;width:420px;font-size:9.5px;line-height:1.6">Curious about our work? See firsthand how we turn spaces into personalized, functional, and beautifully designed environments.</p>
<div class="abs" style="left:93px;top:3972px;width:190px;height:175px;background:var(--metal-copper)"></div>
<div class="abs" style="left:1060px;top:4193px;width:47px;height:170px;background:var(--metal-copper)"></div>
<div class="photo" role="img" aria-label="Open-plan kitchen and living room with striped rug and night city view" style="left:113px;top:3990px;width:975px;height:355px;background:linear-gradient(100deg,#d8d0c3,#a69b89 40%,#c8bda9 65%,#2d3244)"></div>
<div class="abs round-btn" style="left:558px;top:4368px;border:1.5px solid var(--copper)"><svg width="18" height="10" viewBox="0 0 18 10" fill="none" stroke="var(--copper)" stroke-width="1.5"><path d="M18 5H2M6 1L2 5l4 4"/></svg></div>
<div class="abs round-btn" style="left:602px;top:4368px;background:var(--metal-copper)"><svg width="18" height="10" viewBox="0 0 18 10" fill="none" stroke="#fdf5ee" stroke-width="1.5"><path d="M0 5h16M12 1l4 4-4 4"/></svg></div>

<!-- FOOTER + CONTACT -->
<div class="abs" style="left:0;top:4558px;width:1200px;height:316px;background:linear-gradient(160deg,#c0673f,#9e4a2d 40%,#773521 75%,#5e2716)"></div>
<div class="abs" style="left:113px;top:4471px;width:975px;height:163px;background:linear-gradient(120deg,#e8bf9f,#dcae8c 60%,#d29a74);border-bottom:2px solid var(--gilt)"></div>
<div class="abs ghost" style="left:113px;top:4545px;font-size:84px;color:rgba(119,53,33,.12);width:975px">REDEFINING SPACES</div>
<div class="abs label" style="left:203px;top:4519px;color:var(--copper-dark)">Contact</div>
<h2 class="abs heading" style="left:203px;top:4536px;font-size:36px;color:var(--copper-deep)">GET IN TOUCH</h2>
<p class="abs" style="left:672px;top:4523px;font-size:9.5px;color:var(--ink)">Plovar Designs is driven by a passion for both the art of design</p>
<span class="abs btn" style="left:672px;top:4545px;width:120px;height:30px;line-height:30px">SIGN ME UP!</span>

<div class="abs brand" style="left:113px;top:4738px;color:var(--gilt-light);font-size:13px;gap:6px"><span class="mark" style="background:var(--gilt-light);width:11px;height:11px"></span>Plovar Designs</div>
<p class="abs" style="left:275px;top:4700px;width:165px;font-size:9px;line-height:1.6;color:var(--light)">We transform your existing spaces into reflections of your personality and lifestyle.</p>
<div class="abs" style="left:275px;top:4754px;display:flex;gap:10px"><span class="social"></span><span class="social"></span><span class="social"></span><span class="social"></span></div>
<div class="abs footer-col" style="left:545px;top:4676px"><h6>USEFULL LINKS</h6><ul><li>HOME</li><li>ABOUT</li><li>PROJECTS</li></ul></div>
<div class="abs footer-col" style="left:707px;top:4712px"><ul><li>RESOURCES/BLOG</li><li>WHY CHOOSE US</li><li>INQUIRE NOW</li></ul></div>
<div class="abs footer-col" style="left:901px;top:4676px"><h6>OUR GALLERY</h6></div>
<div class="photo" role="img" aria-label="Gallery thumbnail: living room" style="left:901px;top:4700px;width:90px;height:46px;background:linear-gradient(135deg,#cfc3b0,#7d7367)"></div>
<div class="photo" role="img" aria-label="Gallery thumbnail: lounge with view" style="left:997px;top:4700px;width:90px;height:46px;background:linear-gradient(135deg,#e6ddd0,#8f8677)"></div>
<div class="photo" role="img" aria-label="Gallery thumbnail: bedroom" style="left:901px;top:4752px;width:90px;height:46px;background:linear-gradient(135deg,#dcd6cd,#34405a)"></div>
<div class="photo" role="img" aria-label="Gallery thumbnail: dining area" style="left:997px;top:4752px;width:90px;height:46px;background:linear-gradient(135deg,#d4c9b8,#6f6b5f)"></div>
<p class="abs" style="left:0;top:4850px;width:1200px;text-align:center;font-size:8.5px;color:var(--gilt-light)">© 2024 PLOVAR DESIGNS, ALL RIGHTS RESERVED.</p>

</body>
</html>
```